Pomme Sauvage Riding School Flyer Design

We need a flyer for our Horse riding school, called Pomme Sauvage Riding School.

At Pomme Sauvage Riding School, Horses and ponies are carefully matched to suit each rider's experience, ability and confidence. I am a Qualified instructor, equipped to train all levels from nervous beginners to the more advanced.

Horse riding is fun! Riders, particularly children, are taught not only skills on the horse, but skills that are integral to good horsemanship and ownership of horses.

We regularly host Ladies Days, Guest Instructors, 1 hour Trail Rides and Pony Ride Days!

We teach people how to interact safely with, and care for horses so they develop a genuine love and respect for the animals and the sport.

In addition to fundamental riding techniques including walk, trot, and canter, we teach our students:
Grooming and Care of horses, Safety around horses, Balance and Co-Ordination, How to saddle up and care for Tack, Responsibility for equipment and horse, Confidence and Confidence Building for all Ages.

Private and group lessons start at 5 years of age upwards.

We recommend children 4 years and under partake in 15 minute pony rides, mainly due to their attention span!

```html
<!DOCTYPE html>
<html lang="en">
<head>
<meta charset="utf-8">
<title>Pomme Sauvage Riding School Flyer</title>
<link rel="stylesheet" href="https://fonts.googleapis.com/css2?family=Kaushan+Script&family=Josefin+Sans:wght@400;600&family=Open+Sans:wght@400;600;700&display=swap">
<style>
  :root {
    --orange: #f6a21e;
    --pill: #f8aa26;
    --green: #1e7a3b;
    --red: #c7163b;
    --ink: #2b1c12;
    --white: #ffffff;
    --cream: #fff3c4;
    --photo-light: #f3d9a8;
    --photo-mid: #b98a55;
    --photo-dark: #4a3222;
  }
  * { margin: 0; padding: 0; box-sizing: border-box; }
  html, body { width: 1200px; height: 850px; overflow: hidden; background: #ffffff; }
  .flyer {
    position: relative; width: 1200px; height: 850px; overflow: hidden;
    font-family: "Open Sans", Arial, sans-serif;
  }
  .brand-panel {
    position: absolute; left: 0; top: 0; width: 622px; height: 384px;
    background: var(--orange);
  }
  .brand-name {
    position: absolute; left: 0; width: 100%; top: 246px; text-align: center;
    font-family: "Josefin Sans", Arial, sans-serif; font-weight: 400;
    color: var(--ink); line-height: 1;
  }
  .brand-name .name-main { display: block; font-size: 42px; letter-spacing: 6px; }
  .brand-name .name-sub { display: block; font-size: 21px; letter-spacing: 6px; margin-top: 18px; }
  .address {
    position: absolute; left: 0; width: 100%; top: 352px; text-align: center;
    font-size: 18px; color: var(--white);
  }
  .hero-photo {
    position: absolute; left: 622px; top: 0; width: 578px; height: 384px;
    background:
      radial-gradient(ellipse at 30% 20%, var(--photo-light) 0%, transparent 60%),
      linear-gradient(100deg, var(--photo-dark) 0%, var(--photo-mid) 45%, var(--photo-light) 70%, var(--photo-dark) 100%);
  }
  .tagline-band {
    position: absolute; left: 0; top: 384px; width: 1200px; height: 79px;
    background: var(--green);
    display: flex; align-items: center; justify-content: center;
  }
  .tagline {
    font-family: "Kaushan Script", cursive; font-weight: 400;
    font-size: 37px; color: var(--white);
  }
  .info-panel {
    position: absolute; left: 0; top: 463px; width: 1200px; height: 387px;
    background: var(--red);
  }
  .intro {
    position: absolute; left: 68px; top: 32px; width: 520px;
    font-size: 17px; line-height: 22px; color: var(--white);
  }
  .skills {
    position: absolute; left: 114px; top: 92px; list-style: none;
    font-size: 17px; color: var(--white);
  }
  .skills li { position: relative; height: 35.5px; line-height: 22px; padding-left: 26px; }
  .skills li::before {
    content: ""; position: absolute; left: 0; top: 6px;
    width: 11px; height: 11px; border-radius: 50%; background: var(--white);
  }
  .lessons {
    position: absolute; left: 70px; top: 302px;
    font-size: 23px; line-height: 30px; font-weight: 700; color: var(--white);
  }
  .events {
    position: absolute; left: 825px; top: 32px; width: 290px; list-style: none;
  }
  .events li {
    height: 56px; margin-bottom: 4px; border-radius: 14px;
    background: var(--pill); color: var(--ink);
    display: flex; align-items: center; justify-content: center;
    font-size: 25px;
  }
  .call-now {
    position: absolute; left: 618px; top: 290px;
    font-family: "Kaushan Script", cursive; font-weight: 400;
    font-size: 58px; color: var(--cream); white-space: nowrap;
  }
</style>
</head>
<body>
<div class="flyer">
  <section class="brand-panel">
    <h1 class="brand-name">
      <span class="name-main">POMME SAUVAGE</span>
      <span class="name-sub">RIDING SCHOOL</span>
    </h1>
    <p class="address">Wattle Rd, Seabrook</p>
  </section>

  <div class="hero-photo" role="img" aria-label="Photo of a smiling young couple standing with two brown horses in warm evening sunlight"></div>

  <div class="tagline-band">
    <p class="tagline">We teach people how to ride and interact safely with horses.</p>
  </div>

  <section class="info-panel">
    <p class="intro">In addition to fundamental riding techniques including walk, trot, and canter, we teach our students:</p>
    <ul class="skills">
      <li>Grooming and Care of horses,</li>
      <li>Safety around horses,</li>
      <li>Balance and Co-Ordination,</li>
      <li>How to saddle up and care for Tack,</li>
      <li>Responsibility for equipment and horse.</li>
    </ul>
    <p class="lessons">Private and group lessons<br>start at 5 years of age</p>

    <ul class="events">
      <li>Ladies Days,</li>
      <li>Guest Instructors</li>
      <li>1 hour Trail Rides</li>
      <li>Pony Ride Days</li>
    </ul>

    <p class="call-now">Call now 0400 555 018</p>
  </section>
</div>
</body>
</html>
```